Business Card Design Project

The business card is for an educational company that provides personalised tuition to students.

The company logo is in orange and blue (as provided) and should be included in the name card design

The philosophy of the company is to make learning a comfortable experience for student as such design of the namecard should look fresh and has a bit of the 'wow' factor. Some of the namecard design that appeals to me are as uploaded under Sample Design.

The particulars that need to be provided are:
(1): Company Name (Quillmark Education)
(1): Name
(2): Educational qualifications which will appear below name
(3): Mobile number
(4): Email address
(5): Website

Industry/Entity Type

Business

Requirements
Must have
• (1): Company Logo

(2): The card background should preferably be coloured both for the front side and back.

(3): The choice of font is important as part of the selection consideration. There is no preferred font that I have selected, designer is free to choose the font that will complement their design.

```html
<!DOCTYPE html>
<html lang="en">
<head>
<meta charset="utf-8">
<title>Quillmark Education – Business Card</title>
<link rel="stylesheet" href="https://fonts.googleapis.com/css2?family=Sorts+Mill+Goudy&family=Arvo:wght@700&family=Questrial&display=swap">
<style>
  :root {
    --backdrop: #3b3b3b;
    --blue-deep: #2b72ad;
    --blue: #3688c4;
    --blue-light: #3fa3da;
    --orange: #f39a2a;
    --orange-deep: #e9521f;
    --white: #ffffff;
    --ink-grey: #555557;
  }
  * { margin: 0; padding: 0; box-sizing: border-box; }
  html, body {
    width: 1200px;
    height: 900px;
    overflow: hidden;
    background: var(--backdrop);
  }
  .stage { position: relative; width: 1200px; height: 900px; }
  .card {
    position: absolute;
    top: 307px;
    width: 513px;
    height: 285px;
    border-radius: 16px;
    overflow: hidden;
    box-shadow: 0 3px 10px rgba(0,0,0,0.45);
  }
  .card--front { left: 73px; }
  .card--back { left: 615px; background: var(--white); }
  .card svg.card__art { position: absolute; inset: 0; width: 100%; height: 100%; }

  .front__name {
    position: absolute;
    left: 315px;
    top: 106px;
    font-family: "Sorts Mill Goudy", Georgia, serif;
    font-size: 37px;
    line-height: 38px;
    color: var(--white);
  }

  .back__brand {
    position: absolute;
    left: 100px;
    top: 35px;
    display: flex;
    align-items: center;
    gap: 14px;
  }
  .brand__square {
    width: 90px;
    height: 90px;
    border-radius: 10px;
    background: var(--orange);
    flex: none;
  }
  .brand__name {
    font-family: "Sorts Mill Goudy", Georgia, serif;
    font-size: 40px;
    line-height: 40px;
    color: var(--ink-grey);
  }

  .back__details {
    position: absolute;
    left: 205px;
    top: 166px;
    color: var(--white);
  }
  .person__name {
    font-family: "Arvo", Georgia, serif;
    font-weight: 700;
    font-size: 19px;
    line-height: 22px;
  }
  .person__title {
    font-family: "Questrial", Arial, sans-serif;
    font-size: 14px;
    line-height: 16px;
  }
  .contact { list-style: none; margin-top: 9px; }
  .contact li {
    display: flex;
    align-items: center;
    gap: 6px;
    font-family: "Questrial", Arial, sans-serif;
    font-size: 13px;
    line-height: 16px;
  }
  .contact svg { width: 10px; height: 10px; flex: none; }
</style>
</head>
<body>
<main class="stage">

  <section class="card card--front" aria-label="Card front">
    <svg class="card__art" viewBox="0 0 513 285" preserveAspectRatio="none">
      <defs>
        <radialGradient id="frontOrange" cx="0.92" cy="0.5" r="0.7">
          <stop offset="0" stop-color="var(--orange-deep)"/>
          <stop offset="0.55" stop-color="var(--orange)"/>
          <stop offset="1" stop-color="var(--orange)"/>
        </radialGradient>
        <radialGradient id="frontBlue" cx="0.45" cy="0.35" r="0.6">
          <stop offset="0" stop-color="var(--blue-light)"/>
          <stop offset="1" stop-color="var(--blue-deep)"/>
        </radialGradient>
      </defs>
      <rect width="513" height="285" fill="url(#frontOrange)"/>
      <path d="M0 0 H375 C270 40 170 140 125 285 H0 Z" fill="url(#frontBlue)"/>
    </svg>
    <div class="front__name">Quillmark<br>Education</div>
  </section>

  <section class="card card--back" aria-label="Card back">
    <svg class="card__art" viewBox="0 0 513 285" preserveAspectRatio="none">
      <path d="M0 151 C170 154 360 144 513 128 V285 H0 Z" fill="var(--blue)"/>
      <path d="M70 146 C220 150 380 136 513 112 V124 C380 142 220 152 70 146 Z" fill="var(--orange-deep)"/>
    </svg>

    <div class="back__brand">
      <span class="brand__square" aria-hidden="true"></span>
      <span class="brand__name">Quillmark<br>Education</span>
    </div>

    <div class="back__details">
      <p class="person__name">Daniel Harrow</p>
      <p class="person__title">dr. of philosophy</p>
      <ul class="contact">
        <li>
          <svg viewBox="0 0 10 10" aria-hidden="true"><rect x="2.5" y="0.5" width="5" height="9" rx="1" fill="none" stroke="var(--white)" stroke-width="1.2"/></svg>
          555 214 37 90
        </li>
        <li>
          <svg viewBox="0 0 10 10" aria-hidden="true"><rect x="0.5" y="2" width="9" height="6" fill="var(--white)"/><path d="M0.5 2 L5 5.5 L9.5 2" fill="none" stroke="var(--blue)" stroke-width="0.9"/></svg>
          info@quillmarkeducation.com
        </li>
        <li>
          <svg viewBox="0 0 10 10" aria-hidden="true"><circle cx="5" cy="5" r="4.4" fill="none" stroke="var(--white)" stroke-width="1"/><path d="M0.6 5 H9.4 M5 0.6 C2.5 3 2.5 7 5 9.4 M5 0.6 C7.5 3 7.5 7 5 9.4" fill="none" stroke="var(--white)" stroke-width="0.8"/></svg>
          www.quillmarkeducation.com
        </li>
      </ul>
    </div>
  </section>

</main>
</body>
</html>
```